Steelcrest Process Systems. Needs a Business Card Design

We need a business card design for an engineering company which supplies industrial components (pumps, compressors, mechanical seals) provides repairs and services for above mentioned equipments. We offer a uniqe engineering solutions which help our customers to increase the productivness of their manufacturings, and energy savings.

Target Market(s)

Chemical and energy plants, refineries. Food industry and private consumers in a less.

Industry/Entity Type

Business

Contact Information for Business Card

Stylish and sleek design oriented on industrial area.

Requirements
Should not have
• company name shortening

```html
<!DOCTYPE html>
<html lang="en">
<head>
<meta charset="utf-8">
<title>Steelcrest Process Systems – Business Card</title>
<link rel="stylesheet" href="https://fonts.googleapis.com/css2?family=Baloo+2:wght@600;700&family=Arimo:wght@400;700&display=swap">
<style>
  :root {
    --brand-blue: #1f3f93;
    --brand-blue-light: #3a5bb0;
    --brand-blue-dark: #183378;
    --accent-orange: #f7a731;
    --accent-red: #e8412c;
    --card-white: #f4f4f4;
    --page-bg: #2a2a2a;
    --heading-font: "Baloo 2", sans-serif;
    --body-font: "Arimo", sans-serif;
  }
  * { box-sizing: border-box; margin: 0; padding: 0; }
  html, body { width: 1200px; height: 900px; overflow: hidden; }
  body {
    background: var(--page-bg);
    display: flex;
    align-items: center;
    justify-content: center;
    gap: 40px;
    font-family: var(--body-font);
  }
  .card {
    width: 540px;
    height: 310px;
    border-radius: 16px;
    overflow: hidden;
    position: relative;
    box-shadow: 0 10px 30px rgba(0,0,0,.5);
  }

  /* Front */
  .card-front {
    background: radial-gradient(ellipse at 55% 30%, var(--brand-blue-light), var(--brand-blue) 60%, var(--brand-blue-dark));
  }
  .front-brand {
    position: absolute;
    top: 0; left: 0; right: 0;
    height: 270px;
    display: flex;
    flex-direction: column;
    align-items: center;
    justify-content: center;
    gap: 14px;
  }
  .brand-dot {
    width: 74px; height: 74px;
    border-radius: 50%;
    background: var(--accent-orange);
  }
  .front-brand .brand-name {
    font-family: var(--heading-font);
    font-weight: 700;
    font-size: 34px;
    color: #fff;
    line-height: 1;
  }
  .front-strip {
    position: absolute;
    left: 0; right: 0; bottom: 0;
    height: 40px;
    background: #fff;
    display: flex;
    align-items: center;
    justify-content: flex-end;
    padding-right: 40px;
  }
  .front-strip .web {
    font-weight: 700;
    font-size: 15px;
    color: var(--brand-blue);
    letter-spacing: .3px;
  }

  /* Back */
  .card-back { background: var(--card-white); }
  .back-brand {
    position: absolute;
    top: 26px; left: 0; right: 0;
    display: flex;
    flex-direction: column;
    align-items: center;
    gap: 8px;
  }
  .back-brand .brand-dot { width: 56px; height: 56px; }
  .back-brand .brand-name {
    font-family: var(--heading-font);
    font-weight: 700;
    font-size: 26px;
    color: var(--brand-blue);
    line-height: 1;
  }
  .back-details {
    position: absolute;
    top: 142px;
    left: 0; right: 0;
    display: flex;
    justify-content: center;
  }
  .person {
    width: 200px;
    text-align: right;
    padding-right: 18px;
  }
  .person-name {
    font-weight: 700;
    font-size: 19px;
    color: var(--brand-blue);
  }
  .person-title {
    font-size: 12px;
    color: var(--accent-red);
    margin-top: 1px;
  }
  .person-address {
    font-size: 15px;
    color: var(--accent-red);
    margin-top: 32px;
    line-height: 1.2;
  }
  .divider {
    width: 1.5px;
    height: 120px;
    background: var(--brand-blue);
  }
  .contacts {
    list-style: none;
    padding-left: 18px;
    width: 230px;
  }
  .contacts li {
    display: flex;
    align-items: center;
    gap: 10px;
    font-size: 15px;
    color: var(--accent-red);
    height: 24px;
  }
  .contacts svg { width: 16px; height: 16px; flex: none; }
  .check-band {
    position: absolute;
    left: 0; right: 0; bottom: 0;
    height: 26px;
    display: grid;
    grid-template-columns: repeat(4, 1fr);
    grid-template-rows: 1fr 1fr;
  }
  .band-blue { background: var(--brand-blue); }
  .band-orange { background: var(--accent-orange); }
</style>
</head>
<body>

<section class="card card-front">
  <div class="front-brand">
    <span class="brand-dot"></span>
    <span class="brand-name">Steelcrest Process Systems</span>
  </div>
  <div class="front-strip">
    <span class="web">www.steelcrest-ps.com</span>
  </div>
</section>

<section class="card card-back">
  <div class="back-brand">
    <span class="brand-dot"></span>
    <span class="brand-name">Steelcrest Process Systems</span>
  </div>

  <div class="back-details">
    <div class="person">
      <p class="person-name">Your Name</p>
      <p class="person-title">Title</p>
      <p class="person-address">Your Address in<br>just two Line</p>
    </div>
    <div class="divider"></div>
    <ul class="contacts">
      <li>
        <svg viewBox="0 0 16 16" fill="none" stroke="#f7a731" stroke-width="1.4"><circle cx="8" cy="8" r="7"/><path d="M5.5 4.5l1.5 1.5-1 1a5 5 0 0 0 3 3l1-1 1.5 1.5-1 1.2C7.5 12 4 8.5 4.3 5.5z"/></svg>
        88-450-2718
      </li>
      <li>
        <svg viewBox="0 0 16 16" fill="none" stroke="#f7a731" stroke-width="1.4"><rect x="4.5" y="1.5" width="7" height="13" rx="1.2"/><line x1="7" y1="12.3" x2="9" y2="12.3"/></svg>
        88-450-3906
      </li>
      <li>
        <svg viewBox="0 0 16 16" fill="none" stroke="#f7a731" stroke-width="1.4"><rect x="1.5" y="3.5" width="13" height="9"/><path d="M1.5 3.5L8 9l6.5-5.5"/></svg>
        info@steelcrest-ps.com
      </li>
      <li>
        <svg viewBox="0 0 16 16" fill="none" stroke="#f7a731" stroke-width="1.3"><circle cx="8" cy="8" r="6.5"/><ellipse cx="8" cy="8" rx="3" ry="6.5"/><line x1="1.5" y1="8" x2="14.5" y2="8"/></svg>
        www.steelcrest-ps.com
      </li>
    </ul>
  </div>

  <div class="check-band">
    <span class="band-blue"></span><span class="band-orange"></span><span class="band-blue"></span><span class="band-orange"></span>
    <span class="band-orange"></span><span class="band-blue"></span><span class="band-orange"></span><span class="band-blue"></span>
  </div>
</section>

</body>
</html>
```